Business Card for QRB Farmstock

Custom Business Card Brief:
1. We need two designs for this single client, QRB Farmstock LLC and both designs will end up with rounded corner printed cards that fit the PRINTLY.com design format for their special printing style.
2. My client needs two separate card designs since half of their target market is for farm owners in the Cattle and Beef world. The other half of their target market is working with Equine aka Horse farm owners.
3. The look for two card designs can be similar to ensure branding consistency but we will need some space sizing differences so the cards stand out differently in regards to how the services mentioned are laid out on the front of each card design.
4. Both card designs require the front of the card holding all of the great design work. The back of these 2-sided cards will remain white and can just have the contact information listed "again" on the back to match the contact information provided on the front.
5. Card Design 1 will be for Equine customers, Card Design 2 will be for his Cattle/Beef customers.
6. Card Design 1 (Equine) we are thinking we set aside 70% of the card to be dedicated to the Services listed section while the remaining 30% of the front of the card space will hold a smaller logo image space along with his name and contact information.
7. Card Design 2 (Cattle/Beef) we will need opposite of my last point. We want 70% of the card dedicated to a larger logo space and his contact information while the remaining 30% listing the services provided.
8. Card Design #1 - Equine - his Services space should include:
- Equine Mortality Services
- General Removal
- Cremation
- Transportation for Necropsy
9. Card Design #2 - Cattle/Beef - his Services space should include: General Livestock Services, Hauling, Order Buying, Dealing, Dead Stock Removal
10. Contact Information for both card designs:
- Gerald R. Fenwick (owner)
- QRB Farmstock LLC (company)
- 555-318-4692 (phone)
- info@qrbfarmstockservices.example (email)
- QRBFarmstockServices.example (website)
11. Additional Branding Details - The color codes aka pantone colors that are in the current logo file design:
- Blue Pantone 7686C
- Grey Pantone 422C
12. The font styles used in the logo:
- Nexa Bold
- Nexa Rust Slab Black Shadow
13. Back of both card designs, just list his contact information in larger size to stand out more on the white back:
- 555-318-4692 (phone)
Updates

Okay thanks for confirming that our final design files will be ready for the PRINTLY.com format. I noticed the 2nd place vertical card already had rounded corners but the horizontal design that was in 1st place still had sharp square corners. When using the PRINTLY.com format we will be rounding all of the corners of both cards for print. So we just wanted to make sure that both sets of files will be in a rounded design meeting their format sizing to ensure no content from your great designs gets cut off. Thank you again for your attention to detail. ~ Derek

Target Market(s)

Business to Business

Industry/Entity Type

Farming, Agriculture, Livestock

Contact Information for Business Card

Clients' logo, his contact info, and his different services on two similar final card designs.

Font styles to use
Other font styles liked:
• Look at the brief to see how his logo fonts are currently.

Requirements
Must have
• Two versions of the card, one for the Equine horse market, and one for the Cattle/Beef market of farming.
Nice to have
• Clean, sharp, concise.
Should not have
• No flashy or cartoony designs.

```html
<!DOCTYPE html>
<html lang="en">
<head>
<meta charset="utf-8">
<title>QRB Farmstock – Business Cards</title>
<link rel="stylesheet" href="https://fonts.googleapis.com/css2?family=Lexend:wght@400;500;600;700&family=Alfa+Slab+One&display=swap">
<style>
  :root {
    --brand-blue: #1f4f98;
    --brand-navy: #172f5c;
    --brand-grey: #b9bcc1;
    --dot-grey: #a7abb1;
    --rule-grey: #c4c7cc;
    --card-white: #ffffff;
    --page-bg: #e9e6e1;
    --text-font: "Lexend", sans-serif;
    --slab-font: "Alfa Slab One", serif;
  }
  * { margin: 0; padding: 0; box-sizing: border-box; }
  html, body { width: 1200px; height: 802px; overflow: hidden; }
  body { background: var(--page-bg); position: relative; font-family: var(--text-font); }

  .card {
    position: absolute;
    width: 450px; height: 302px;
    border-radius: 14px;
    overflow: hidden;
    background: var(--card-white);
    box-shadow: 0 4px 10px rgba(0,0,0,0.25);
  }
  .card--equine-front { left: 75px; top: 67px; }
  .card--cattle-front { left: 677px; top: 67px; }
  .card--equine-back  { left: 75px; top: 428px; }
  .card--cattle-back  { left: 677px; top: 428px; }

  .card__shapes { position: absolute; inset: 0; }
  .abs { position: absolute; white-space: nowrap; }
  .center { transform: translateX(-50%); text-align: center; }

  .brand-name { font-weight: 700; color: var(--brand-blue); font-size: 23px; letter-spacing: 0.2px; }
  .brand-town { font-size: 8px; color: var(--brand-grey); letter-spacing: 0.6px; font-weight: 500; }
  .brand-phone { font-weight: 600; color: var(--brand-navy); font-size: 19px; }

  .contact-name { color: #fff; font-weight: 600; font-size: 12.5px; letter-spacing: 0.2px; }
  .contact-dots { color: var(--dot-grey); font-size: 10px; letter-spacing: 2px; line-height: 1; }
  .contact-line { color: #fff; font-size: 10px; font-weight: 400; letter-spacing: 0.2px; }

  .services { position: absolute; }
  .services__item {
    position: relative; color: #fff; text-transform: uppercase; font-weight: 500;
    border-bottom: 1px solid rgba(255,255,255,0.55);
  }
  .services__item:last-child { border-bottom: none; }
  .services__item::before {
    content: ""; position: absolute; border-radius: 50%; background: var(--dot-grey);
  }
  .services__item--plain::before { display: none; }

  .services--equine { left: 31px; top: 74px; width: 193px; }
  .services--equine .services__item { font-size: 14.5px; line-height: 21px; padding: 3px 0 4px 18px; }
  .services--equine .services__item::before { width: 9px; height: 9px; left: 2px; top: 9px; }

  .services--cattle { left: 279px; top: 91px; width: 146px; }
  .services--cattle .services__item { font-size: 10.5px; line-height: 16px; padding: 2px 0 3px 17px; }
  .services--cattle .services__item::before { width: 9px; height: 9px; left: 1px; top: 5px; }

  .back__title { font-family: var(--slab-font); color: var(--brand-blue); font-size: 29px; letter-spacing: 0.5px; top: 66px; left: 225px; }
  .back__name { color: var(--brand-blue); font-weight: 700; font-size: 20px; top: 111px; left: 225px; }
  .back__rule { position: absolute; top: 151px; height: 1px; background: var(--rule-grey); }
  .back__rule--left { left: 0; width: 182px; }
  .back__rule--right { left: 268px; right: 0; }
  .back__icons { position: absolute; top: 141px; left: 191px; }
  .back__line { color: var(--brand-blue); font-weight: 500; font-size: 18px; left: 225px; }
</style>
</head>
<body>

<!-- Equine front -->
<section class="card card--equine-front" aria-label="Equine card front">
  <svg class="card__shapes" viewBox="0 0 450 302" aria-hidden="true">
    <rect width="450" height="302" fill="var(--brand-blue)"/>
    <polygon points="121,0 450,0 450,124 340,187" fill="var(--card-white)"/>
    <polygon points="86,237 162,302 6,302" fill="var(--brand-grey)"/>
  </svg>
  <div class="abs center brand-name" style="left:340px; top:52px;">QRB Farmstock</div>
  <div class="abs center brand-town" style="left:340px; top:98px;">Millbrook, PA</div>
  <div class="abs center brand-phone" style="left:340px; top:107px;">555-318-4692</div>

  <ul class="services services--equine" style="list-style:none;">
    <li class="services__item">Equine Mortality<br>Services</li>
    <li class="services__item">General Removal</li>
    <li class="services__item">Cremation</li>
    <li class="services__item">Transportation for<br>Necropsy</li>
  </ul>

  <div class="abs center contact-name" style="left:340px; top:207px;">GERALD R. FENWICK</div>
  <div class="abs center contact-dots" style="left:340px; top:227px;">•••</div>
  <div class="abs center contact-line" style="left:340px; top:240px;">555-318-4692</div>
  <div class="abs center contact-line" style="left:340px; top:255px;">info@qrbfarmstockservices.example</div>
  <div class="abs center contact-line" style="left:340px; top:270px;">QRBFarmstockServices.example</div>
</section>

<!-- Cattle front -->
<section class="card card--cattle-front" aria-label="Cattle card front">
  <svg class="card__shapes" viewBox="0 0 450 302" aria-hidden="true">
    <rect width="450" height="302" fill="var(--brand-blue)"/>
    <polygon points="0,0 393,0 140,204 0,88" fill="var(--card-white)"/>
    <polygon points="350,243 433,302 271,302" fill="var(--brand-grey)"/>
  </svg>
  <div class="abs center brand-name" style="left:139px; top:62px; font-size:26px;">QRB Farmstock</div>
  <div class="abs center brand-town" style="left:139px; top:111px; font-size:9px;">Millbrook, PA</div>
  <div class="abs center brand-phone" style="left:139px; top:121px; font-size:20px;">555-318-4692</div>

  <ul class="services services--cattle" style="list-style:none;">
    <li class="services__item">General Livestock<br>Services</li>
    <li class="services__item services__item--plain">Hauling</li>
    <li class="services__item">Order Buying</li>
    <li class="services__item">Dealing</li>
    <li class="services__item">Dead Stock Removal</li>
  </ul>

  <div class="abs center contact-name" style="left:136px; top:205px;">GERALD R. FENWICK</div>
  <div class="abs center contact-dots" style="left:136px; top:224px;">•••</div>
  <div class="abs center contact-line" style="left:136px; top:235px;">555-318-4692</div>
  <div class="abs center contact-line" style="left:136px; top:250px;">info@qrbfarmstockservices.example</div>
  <div class="abs center contact-line" style="left:136px; top:265px;">QRBFarmstockServices.example</div>
</section>

<!-- Backs -->
<section class="card card--equine-back" aria-label="Equine card back">
  <div class="abs center back__title">QRB FARMSTOCK LLC</div>
  <div class="abs center back__name">GERALD R. FENWICK</div>
  <div class="back__rule back__rule--left"></div>
  <div class="back__rule back__rule--right"></div>
  <svg class="back__icons" width="68" height="20" viewBox="0 0 68 20" aria-hidden="true">
    <g fill="var(--brand-grey)"><circle cx="9" cy="10" r="9"/><circle cx="34" cy="10" r="9"/><circle cx="59" cy="10" r="9"/></g>
    <path d="M5.5 6.5c.8 2.8 2.6 5 5.6 6.4l1.3-1.3 1.8 1-.6 1.7c-4.2-.3-7.6-3.8-8-8l1.7-.6 1 1.8z" fill="#fff"/>
    <g fill="none" stroke="#fff" stroke-width="1.1"><rect x="29" y="6.5" width="10" height="7"/><path d="M29 6.5l5 4 5-4"/>
    <circle cx="59" cy="10" r="5"/><path d="M54 10h10M59 5c-2 3-2 7 0 10M59 5c2 3 2 7 0 10"/></g>
  </svg>
  <div class="abs center back__line" style="top:162px;">555-318-4692</div>
  <div class="abs center back__line" style="top:188px; font-size:16px;">info@qrbfarmstockservices.example</div>
  <div class="abs center back__line" style="top:214px;">QRBFarmstockServices.example</div>
</section>

<section class="card card--cattle-back" aria-label="Cattle card back">
  <div class="abs center back__title">QRB FARMSTOCK LLC</div>
  <div class="abs center back__name">GERALD R. FENWICK</div>
  <div class="back__rule back__rule--left"></div>
  <div class="back__rule back__rule--right"></div>
  <svg class="back__icons" width="68" height="20" viewBox="0 0 68 20" aria-hidden="true">
    <g fill="var(--brand-grey)"><circle cx="9" cy="10" r="9"/><circle cx="34" cy="10" r="9"/><circle cx="59" cy="10" r="9"/></g>
    <path d="M5.5 6.5c.8 2.8 2.6 5 5.6 6.4l1.3-1.3 1.8 1-.6 1.7c-4.2-.3-7.6-3.8-8-8l1.7-.6 1 1.8z" fill="#fff"/>
    <g fill="none" stroke="#fff" stroke-width="1.1"><rect x="29" y="6.5" width="10" height="7"/><path d="M29 6.5l5 4 5-4"/>
    <circle cx="59" cy="10" r="5"/><path d="M54 10h10M59 5c-2 3-2 7 0 10M59 5c2 3 2 7 0 10"/></g>
  </svg>
  <div class="abs center back__line" style="top:162px;">555-318-4692</div>
  <div class="abs center back__line" style="top:188px; font-size:16px;">info@qrbfarmstockservices.example</div>
  <div class="abs center back__line" style="top:214px;">QRBFarmstockServices.example</div>
</section>

</body>
</html>
```